Bref créative
Stationary, Envelope, and Business Card Designs for an Accounting/Bookkeeping company
R&K Ledger and Audit Partners, LLC
Professional
Doug M. Prentt
Partner, Chief Financial Officer
41207 Route 53
Palmera Bay, ST 40217
dprentt@rkbooksco.com
www.rkbooksco.com
R&K Ledger and Audit Partners, LLC Logo in AI format - full color.
Logo color specifics.

```html
<!DOCTYPE html>
<html lang="en">
<head>
<meta charset="utf-8">
<title>R&amp;K Ledger and Audit Partners — Stationery</title>
<link href="https://fonts.googleapis.com/css2?family=Open+Sans:wght@400;600&display=swap" rel="stylesheet">
<style>
:root{
  --bg:#eceef0;
  --paper:#ffffff;
  --blue:#1f3f98;
  --blue-light:#3a5fc0;
  --green:#7dbb2f;
  --ink:#3c4655;
  --muted:#8a93a0;
  --faint:#eef2f8;
}
*{margin:0;padding:0;box-sizing:border-box}
html,body{width:1200px;height:936px;overflow:hidden}
body{background:var(--bg);position:relative;font-family:"Open Sans",sans-serif;color:var(--ink)}
.sheet{position:absolute;background:var(--paper);overflow:hidden}

.brand{display:flex;align-items:center;gap:8px;color:var(--blue);font-family:"Open Sans",sans-serif;font-weight:600;line-height:1.2}
.brand-dot{border-radius:50%;background:var(--blue);flex:none}
.brand-name{display:block}

/* plain footer band: thin green rule above a flat blue band */
.band{position:absolute;left:0;bottom:0;width:100%;background:var(--blue)}
.band::before{content:"";position:absolute;left:0;right:0;top:-7px;height:3px;background:var(--green)}

.letterhead{left:182px;top:68px;width:387px;height:539px}
.letterhead .brand{position:absolute;left:26px;top:26px;font-size:9px;width:180px}
.letterhead .brand-dot{width:20px;height:20px}
.contact{position:absolute;right:30px;top:20px;font-size:5.5px;line-height:9px;color:var(--muted);list-style:none}
.contact li{display:flex;align-items:center;gap:4px}
.contact li::before{content:"";width:4px;height:4px;border-radius:50%;background:var(--blue-light)}
.backdrop-mark{position:absolute;left:128px;top:200px;width:130px;height:130px;border-radius:50%;background:var(--faint)}
.letterhead .band{height:34px}

.folder{left:635px;top:51px;width:491px;height:569px}
.folder .brand{position:absolute;left:70px;top:236px;font-size:22px;gap:16px;width:360px}
.folder .brand-dot{width:60px;height:60px}
.folder .band{height:44px}

.card{width:202px;height:113px}
.card-front{left:43px;top:670px}
.card-front .brand{position:absolute;left:14px;top:12px;font-size:6.5px;gap:6px;width:170px}
.card-front .brand-dot{width:16px;height:16px}
.card-front .person{position:absolute;left:36px;top:40px;font-size:5px;line-height:7px;color:var(--muted)}
.card-front .person strong{color:var(--ink);font-weight:600}
.card-front .band{height:12px}
.card-back{left:43px;top:789px}
.card-back .brand-dot{position:absolute;left:87px;top:28px;width:28px;height:28px}
.card-back .web{position:absolute;left:0;right:0;top:88px;text-align:center;font-size:5px;letter-spacing:2px;color:var(--muted)}

.envelope{left:263px;top:670px;width:440px;height:233px}
.envelope .brand{position:absolute;left:18px;top:16px;font-size:8px;gap:6px;width:200px}
.envelope .brand-dot{width:22px;height:22px}
.envelope .return{position:absolute;left:46px;top:46px;font-size:5px;line-height:7px;color:var(--muted)}

.envelope-back{left:736px;top:670px;width:415px;height:233px}
.flap{position:absolute;left:0;top:0;width:100%;height:104px;background:linear-gradient(180deg,var(--blue-light),var(--blue))}
.flap-edge{position:absolute;left:0;top:104px;width:100%;height:4px;background:var(--green)}
.flap .web{position:absolute;left:0;right:0;top:46px;text-align:center;color:#fff;font-size:8px;letter-spacing:4px}
</style>
</head>
<body>

<section class="sheet letterhead">
  <div class="brand"><span class="brand-dot"></span><span class="brand-name">R&amp;K Ledger and Audit Partners, LLC</span></div>
  <ul class="contact">
    <li>41207 Route 53</li>
    <li>Palmera Bay, ST 40217</li>
    <li>(555) 014-2290</li>
    <li>(555) 014-2291</li>
    <li>dprentt@rkbooksco.com</li>
    <li>www.rkbooksco.com</li>
  </ul>
  <div class="backdrop-mark"></div>
  <div class="band"></div>
</section>

<section class="sheet folder">
  <div class="brand"><span class="brand-dot"></span><span class="brand-name">R&amp;K Ledger and Audit Partners, LLC</span></div>
  <div class="band"></div>
</section>

<section class="sheet card card-front">
  <div class="brand"><span class="brand-dot"></span><span class="brand-name">R&amp;K Ledger and Audit Partners, LLC</span></div>
  <p class="person"><strong>Doug M. Prentt</strong><br>Partner, Chief Financial Officer<br>41207 Route 53<br>Palmera Bay, ST 40217<br>dprentt@rkbooksco.com</p>
  <div class="band"></div>
</section>

<section class="sheet card card-back">
  <span class="brand-dot"></span>
  <p class="web">www.rkbooksco.com</p>
</section>

<section class="sheet envelope">
  <div class="brand"><span class="brand-dot"></span><span class="brand-name">R&amp;K Ledger and Audit Partners, LLC</span></div>
  <p class="return">41207 Route 53<br>Palmera Bay, ST 40217</p>
</section>

<section class="sheet envelope-back">
  <div class="flap"><p class="web">www.rkbooksco.com</p></div>
  <div class="flap-edge"></div>
</section>

</body>
</html>
```